FACIAL COSMETICS BUSINESS CARD

WE ARE A DENTAL PRACTICE BUT ARE OPENING UP A BRANCH FOR FACILA COSMETICS, LIKE BOTOX, FILLERS, PEELS, ETC. GWEN AND MARISOL WILL BE RUNNING THAT PART OF THE BUSINESS.
OUR CURRENT CARD IS ATTACHED AND OUR LOGO IT ATTACHED TOO. THE LOGO HAS ON IT OLMEN DENTAL, I WOULD LIKE IT TO SAY OLMEN COSMETICS, THE PHONE NUMBERS ON IT HAS TO BE REPLACED BY THE ONES I GAVE PREVIOUSLY AND THE WEB ADDRESS HAS TO BE DELETED, THE OTHER SIDE OF THE CARD HAS A MAP WHICH HAS TO BE DELETED, ADD TWO DATE-TIME LINES, I LIKE THE CARDS TO BE SIMPLE AND CLEAN, SIZE HAS TO BE NO LARGER THAN 5CMx8.5CM.
THE CARD HAS TO BE MATTE, I HATE GLOSSY, ABLE TO BE WRITTEN ON BOTH SIDES

Updates
I HAVE ATTACHED THE FILES, THEY CONSIST OF OUR CURRENT LOGO IN A FEW FORMS AND OUR BUSINESS CARD FOR THE DENTAL BRANCH, PLEASE COPY THE CURRENT DESIGN BUT ADDING THE REQUESTED CHANGES

Industry/Entity Type
Business
Contact Information for Business Card
OLMEN COSMETICS
GWEN : 0438 517 203
MARISOL : 0419 862 374
SUITE 8 HOLLOWAY COURT ARCADE
47-59 PENDRICK STREET
TALLOWMERE NSW 2389
Logo Text
OLMEN COSMETICS
Look and feel

```html
<!DOCTYPE html>
<html lang="en">
<head>
<meta charset="utf-8">
<title>Olmen Cosmetics – Business Card</title>
<link href="https://fonts.googleapis.com/css2?family=Open+Sans:wght@600&family=Michroma&display=swap" rel="stylesheet">
<style>
  :root {
    --stage: #808080;
    --card: #ffffff;
    --card-fade: #f3f4f4;
    --green: #3dae49;
    --ink: #111111;
    --faint-ink: #a9a9a9;
    --faint-green: #cfe5cf;
  }
  * { box-sizing: border-box; margin: 0; padding: 0; }
  html, body { width: 1200px; height: 900px; overflow: hidden; }
  body {
    background: var(--stage);
    position: relative;
    font-family: "Open Sans", Arial, sans-serif;
    color: var(--ink);
  }
  .card {
    position: absolute;
    left: 266px;
    width: 700px;
    background: linear-gradient(to bottom, var(--card) 40%, var(--card-fade));
    overflow: hidden;
  }
  .card--front { top: 22px; height: 413px; }
  .card--back { top: 459px; height: 412px; }
  .card__shapes { position: absolute; inset: 0; }
  .card__shapes path { fill: var(--green); }

  /* Front */
  .brand-mark {
    position: absolute;
    left: 28px; top: 150px;
    width: 290px;
    display: flex; align-items: center; gap: 10px;
    font-weight: 600; font-size: 25px; letter-spacing: 2px;
    color: var(--ink);
  }
  .brand-mark__dot {
    width: 18px; height: 18px; border-radius: 50%;
    background: var(--green); flex: none;
  }
  .corner-mark {
    position: absolute; right: 12px; top: 10px;
    font-weight: 600; font-size: 11px; letter-spacing: 1px;
    color: var(--faint-green);
  }
  .divider {
    position: absolute; left: 345px; top: 41px;
    width: 2px; height: 303px; background: var(--green);
  }
  .title {
    position: absolute; left: 380px; top: 66px; width: 212px;
    text-align: center;
    font-weight: 600; font-size: 33px; line-height: 45px;
  }
  .contacts {
    position: absolute; left: 381px; top: 210px;
    font-weight: 600; font-size: 18px; line-height: 42px;
    letter-spacing: 0.5px;
    list-style: none;
  }
  .contacts__name { display: inline-block; width: 88px; }
  .contacts li:last-child .contacts__name { width: auto; margin-right: 4px; }
  .address {
    position: absolute; left: 0; right: 0; top: 368px;
    text-align: center;
    font-family: "Michroma", Arial, sans-serif;
    font-size: 11px; line-height: 21px; letter-spacing: 3.4px;
    color: var(--ink);
  }

  /* Back */
  .back-mark {
    position: absolute; left: 0; right: 0; top: 58px;
    text-align: center;
    font-weight: 600; font-size: 24px; letter-spacing: 2px;
    color: var(--faint-ink); opacity: .8;
  }
  .appointments { position: absolute; inset: 0; list-style: none; }
  .appointment__field {
    position: absolute;
    font-weight: 600; font-size: 18px; letter-spacing: .5px;
    display: flex; align-items: baseline; gap: 6px;
  }
  .appointment__line {
    display: inline-block; width: 124px;
    border-bottom: 3px dotted var(--green);
    transform: translateY(-2px);
  }
</style>
</head>
<body>

<section class="card card--front" aria-label="Business card front">
  <svg class="card__shapes" viewBox="0 0 700 413" width="700" height="413" aria-hidden="true">
    <path d="M435,0 C560,8 650,42 700,82 V0 Z"/>
    <path d="M0,298 C130,345 290,364 440,363 H700 V413 H0 Z"/>
  </svg>
  <div class="corner-mark">OLMEN</div>
  <div class="brand-mark"><span class="brand-mark__dot"></span>OLMEN COSMETICS</div>
  <div class="divider"></div>
  <h1 class="title">OLMEN<br>Cosmetics</h1>
  <ul class="contacts">
    <li><span class="contacts__name">GWEN</span>: 0438 517 203</li>
    <li><span class="contacts__name">MARISOL</span>: 0419 862 374</li>
  </ul>
  <address class="address" style="font-style:normal">
    SUITE 8 HOLLOWAY COURT ARCADE<br>
    47-59 PENDRICK STREET TALLOWMERE NSW 2389
  </address>
</section>

<section class="card card--back" aria-label="Business card back">
  <svg class="card__shapes" viewBox="0 0 700 412" width="700" height="412" aria-hidden="true">
    <path d="M0,54 C35,34 70,14 110,0 H0 Z"/>
    <path d="M0,402 C310,398 560,362 700,305 V412 H0 Z"/>
  </svg>
  <div class="back-mark">OLMEN COSMETICS</div>
  <ul class="appointments">
    <li>
      <span class="appointment__field" style="left:81px; top:172px">Date : <span class="appointment__line"></span></span>
      <span class="appointment__field" style="left:412px; top:172px">Time : <span class="appointment__line"></span></span>
    </li>
    <li>
      <span class="appointment__field" style="left:83px; top:255px">Date : <span class="appointment__line"></span></span>
      <span class="appointment__field" style="left:414px; top:255px">Time : <span class="appointment__line"></span></span>
    </li>
  </ul>
</section>

</body>
</html>
```